Cruise Booking Website

Cruise search and booking website

This project is a redesign of a cruise booking website we did a few years ago.

The current website is located here: http://voyage.pixelmarsh.com/en/

It's not fully functional but gives you ad idea how miserable the old design was.

All the information about cruises, cruise lines, destinations, ports and shore excursions will be similar to http://www.sailorbay.com/
Actual search pages (form, results, single result, sailing and cabin selection, ship info, booking) will have EXACTLY the same info as sailorbay.com

We like the style of http://harborvoyagehub.com, it's quite modern, good spacing, not overloaded with information. So you can use it as an example of what we like, not what we want as a final result for us. Please, don't copy it. The result should not be possible to resemble the harborvoyagehub.com, because our site has to be unique. This is important!
If you submit a design that clearly reminds another cruise site it will be rejected!

Also the mockup provided is just to give you the basic structure and show what information has to be present on the page. It doesn't mean the layout has to be the same as a mockup. The layout is up to the designer.

I've updated the mockup to be more generic so it doesn't confuse you:
https://www.filecrate.net/s/k7q2mz9pw4tnb3x/Home%20page.png

When you're adding social sharing icons like chatterbox/peeplet you have to use chinese ones instead:
https://www.filecrate.net/s/h3rt8wyd6jcl0fe/chinese-social-icons.png
Originals: http://shrtlk.example/qRmT

We'll start with home page first and after it's approved inner pages can be designed.

I know the cost of the project doesn't look high, but the task is straight forward and doesn't require to be very original, it's better to follow existing design and layout patterns that proved to work well.
That's why I encourage you to choose a template to build the design on top of one of https://themequarry.net/ themes if it will save the design work, will be easier and faster for you. So it will be more like a customization than a new design from scratch.

Mockups, site map and logo files:
- https://www.filecrate.net/sh/50xb7vq1ndtpkez/RmwuHp8Zq3

Website tree:
- https://papers.quillnet.example/document/d/8vTrXk2MqLpZ4wNsB7yHcE1oUjFgD9aR_QbVtnWm/edit?usp=sharing
Updates

So far a lot of designs are just copying http://www.harborvoyagehub.com/ - we don't like it!

We like the style of harborvoyagehub.com, it's quite modern, good spacing, not overloaded with information. So you can use it as an example of what we like, not what we want as a final result for us. Please, don't copy it. The result should not be possible to resemble the harborvoyagehub.com, because our site has to be unique. This is important!

Target Market(s)

Chinese travellers

Industry/Entity Type

Build

Requirements
Must have
• * White, blue and red
* Large spacing, not too much information cramped into a small space like sailorbay.com or the current website
* More "hidden" info in popups, tabs and so on, so not to many things are visible at the same time
* Compatible with lumen framekit styling (for easier coding):
- http://lumenkit.example.io/framework/index.html
- http://skinvault.net/
* Feel free to propose to build the design on top of one of https://themequarry.net/ themes if it will save the design work, will be easier and faster for you

```html
<!DOCTYPE html>
<html lang="en">
<head>
<meta charset="utf-8">
<title>Bluewake – Cruise Booking</title>
<link href="https://fonts.googleapis.com/css2?family=Arimo:ital,wght@0,400;0,700;1,400&family=Ubuntu:wght@500;700&family=Delius&display=swap" rel="stylesheet">
<style>
:root{
  --blue:#1e6fae;
  --blue-dark:#175c93;
  --blue-light:#2a9ad6;
  --text-blue:#1f75b5;
  --ink:#333;
  --nav:#2f2f2f;
  --footer:#353535;
  --footer-text:#a9a9a9;
  --tabbar:#ececec;
  --red:#d6382c;
}
*{box-sizing:border-box;margin:0;padding:0}
html,body{width:986px;height:1200px;overflow:hidden}
body{position:relative;background:#fff;font-family:"Arimo",Arial,sans-serif;color:var(--ink)}
.abs{position:absolute}

/* header */
.brand{left:115px;top:18px;display:flex;align-items:center;gap:10px}
.brand-mark{width:56px;height:56px;border-radius:50%;background:var(--blue)}
.brand-name{font-family:"Ubuntu",sans-serif;font-weight:700;font-size:36px;color:var(--blue-dark);line-height:1}
.brand-url{display:block;font-family:"Ubuntu",sans-serif;font-weight:700;font-size:12px;color:var(--blue-dark);margin-top:4px;letter-spacing:.5px}
.top-social{left:615px;top:7px;display:flex;gap:5px}
.soc{width:19px;height:19px;border-radius:2px}
.account{left:764px;top:7px;display:flex;gap:4px}
.account a{display:block;height:19px;line-height:19px;padding:0 9px;font-size:10px;color:#fff;text-decoration:none}
.btn-signin{background:#555}
.btn-signup{background:var(--blue)}
.callus{left:712px;top:46px;display:flex;gap:8px;align-items:center}
.phone-ic{width:32px;height:32px;border-radius:4px;background:#666;display:flex;align-items:center;justify-content:center}
.callus em{display:block;font-size:15px;color:#444}
.callus strong{display:block;font-size:20px;color:var(--blue);line-height:1.05}

/* nav */
.mainnav{left:0;top:96px;width:986px;height:33px;background:var(--nav)}
.mainnav ul{list-style:none;display:flex;margin-left:118px;height:33px;border-left:1px solid #444}
.mainnav li{font-size:12px;color:#fff;padding:0 12px;line-height:33px;border-right:1px solid #444}

/* hero */
.hero{left:0;top:129px;width:986px;height:371px;background:linear-gradient(180deg,#8fb4d9 0%,#c9dcee 35%,#2d5f94 62%,#17406e 100%)}
.hero-ship{left:95px;top:160px;width:600px;height:250px;background:linear-gradient(180deg,#f3f5f7,#c9d0d6);border-radius:40% 60% 20% 10%/50% 60% 30% 20%;opacity:.9}
.hero-stripe{left:0;top:500px;width:986px;height:3px;background:var(--blue-light)}
.caption{font-size:20px;color:#fff;padding:0 7px;height:31px;line-height:31px}
.cap1{left:116px;top:351px;background:rgba(30,111,174,.85)}
.cap2{left:198px;top:382px;height:33px;line-height:33px;background:rgba(40,40,40,.75)}

/* search */
.search{left:682px;top:196px;width:189px;height:261px;background:#fff}
.search h2{height:36px;line-height:36px;background:var(--blue);color:#fff;text-align:center;font-size:18px;font-weight:700}
.sel{position:absolute;left:11px;width:168px;height:25px;border:1px solid #ddd;background:linear-gradient(#fff,#ececec);font-size:13px;color:#555;padding-left:9px;line-height:23px}
.sel i{position:absolute;right:4px;top:4px;width:15px;height:15px;background:#dfe8f2;border:1px solid #a8c1dc;display:flex;align-items:center;justify-content:center}
.search .more{position:absolute;left:11px;top:204px;font-size:11px;color:var(--blue-light)}
.search .adv{position:absolute;left:11px;top:235px;font-size:11px;color:var(--blue-light)}
.search .go{position:absolute;left:107px;top:231px;width:72px;height:23px;background:var(--blue);color:#fff;font-size:12px;text-align:center;line-height:23px;border-radius:2px}

/* tabs */
.tabbar{left:0;top:503px;width:986px;height:33px;background:var(--tabbar)}
.tabs{left:115px;top:503px;display:flex;list-style:none}
.tabs li{font-size:12px;color:#333;padding:0 14px;line-height:33px;height:33px}
.tabs li.on{background:var(--blue-light);color:#fff;position:relative;padding:0 13px}
.tabs li.on::after{content:"";position:absolute;left:42px;bottom:-8px;border:5px solid transparent;border-top:5px solid var(--blue-light);border-bottom:0;width:0}

/* book */
.photo-frame{left:115px;top:568px;width:259px;height:203px;background:#fff;box-shadow:0 0 3px rgba(0,0,0,.25);padding:6px}
.photo{width:100%;height:100%;background:linear-gradient(160deg,#3d7fbf 0%,#c99c74 45%,#5fb2d8 80%,#9ed6ea 100%)}
.book h1{position:absolute;left:395px;top:568px;font-family:"Ubuntu",sans-serif;font-weight:700;font-size:25px;color:var(--blue)}
.book h3{position:absolute;left:395px;top:604px;font-family:"Delius",cursive;font-weight:400;font-size:20px;color:var(--blue-light)}
.book p{position:absolute;left:395px;top:634px;width:272px;font-size:13px;line-height:15px;text-align:justify;text-align-last:left;color:#333}
.perks{position:absolute;left:395px;top:687px;list-style:none}
.perks li{font-size:12px;color:var(--blue);height:20px;display:flex;align-items:center;gap:6px}
.tick{width:12px;height:12px;border-radius:50%;background:var(--blue-light);display:flex;align-items:center;justify-content:center}

/* newsletter */
.news{left:715px;top:567px;width:156px;height:206px;background:#fff;border-top:3px solid var(--blue);box-shadow:0 0 2px rgba(0,0,0,.2)}
.news h4{font-weight:400;font-size:13px;color:var(--text-blue);padding:8px 0 0 7px;height:34px}
.news .nimg{height:68px;background:linear-gradient(180deg,#4ea8d8,#a8dceb 60%,#e6c5a8)}
.news .sub{font-size:11px;line-height:14px;color:#333;padding:9px 10px 0}
.news .email{position:absolute;left:9px;top:145px;width:138px;height:22px;border:1px solid #ccc;background:#f7f7f7;font-size:9px;color:#333;display:flex;align-items:center;gap:6px;padding-left:5px}
.news .subbtn{position:absolute;left:11px;top:176px;width:72px;height:23px;background:var(--blue);color:#fff;font-size:12px;text-align:center;line-height:23px}

/* partners */
.partners-h{left:115px;top:819px;font-family:"Ubuntu",sans-serif;font-weight:500;font-size:20px;color:var(--blue)}
.badge{top:860px;width:129px;height:53px;background:#fff;box-shadow:0 0 3px rgba(0,0,0,.25);display:flex;align-items:center;justify-content:center}
.badge span{display:block;width:84px;height:16px;border-radius:3px}

/* footer */
.footer{left:0;top:957px;width:986px;height:243px;background:var(--footer)}
.fcol h5{font-size:14px;font-weight:400;color:#fff;margin-bottom:14px}
.fcol ul{list-style:none}
.fcol li{font-size:9.5px;color:var(--footer-text);line-height:18px;letter-spacing:.3px}
.fcol li::before{content:"> ";font-size:8px}
.faddr{font-size:9.5px;color:var(--footer-text);line-height:15px;letter-spacing:.3px}
.fline{display:flex;gap:6px;align-items:center;font-size:9.5px;color:var(--footer-text);line-height:18px;letter-spacing:.3px}
.flogo{left:491px;top:1006px;width:73px;height:92px;background:#fff;display:flex;flex-direction:column;align-items:center;justify-content:center;gap:6px}
.flogo .c{width:40px;height:40px;border-radius:50%;background:var(--blue)}
.flogo b{font-family:"Ubuntu",sans-serif;font-size:12px;color:var(--blue-dark)}
.fdivide{left:115px;top:1142px;width:756px;height:1px;background:#2a2a2a}
.copy{left:115px;top:1157px;font-size:9.5px;line-height:15px;color:var(--footer-text)}
.foot-social{left:749px;top:1159px;display:flex;gap:6px}
.foot-social span{width:20px;height:20px;background:#1f1f1f;border-radius:2px;display:flex;align-items:center;justify-content:center}
.foot-social span i{width:10px;height:10px;border-radius:50%;background:#fff}
</style>
</head>
<body>

<header>
  <div class="abs brand">
    <span class="brand-mark"></span>
    <div><span class="brand-name">Bluewake</span><span class="brand-url">www.bluewake.example</span></div>
  </div>
  <div class="abs top-social">
    <span class="soc" style="background:#3a7bd5"></span>
    <span class="soc" style="background:#e8552d"></span>
    <span class="soc" style="background:#2a9ad6"></span>
    <span class="soc" style="background:#3aa64a"></span>
    <span class="soc" style="background:#e6eef6;border:1px solid #c9d6e4"></span>
    <span class="soc" style="background:#7cc43b"></span>
  </div>
  <div class="abs account"><a class="btn-signin">Sign in</a><a class="btn-signup">Sign up</a></div>
  <div class="abs callus">
    <span class="phone-ic"><svg width="16" height="20" viewBox="0 0 16 20"><path d="M4 1 L7 1 L8 6 L6 7 Q7 12 10 14 L12 12 L15 15 L14 18 Q6 18 3 10 Q1 4 4 1Z" fill="#fff"/></svg></span>
    <div><em>Call Us Today!</em><strong>4008 215 390</strong></div>
  </div>
</header>

<nav class="abs mainnav">
  <ul><li>Home</li><li>Destination</li><li>Cruise Lines</li><li>Shore Excursion</li><li>Cruise Info</li><li>Deals</li><li>Online Booking</li><li>Contact Us</li><li>Blog</li></ul>
</nav>

<section class="abs hero" role="img" aria-label="Large white cruise ship sailing on a deep blue sea under a cloudy sky"></section>
<div class="abs hero-ship" role="img" aria-label="Cruise ship hull and decks"></div>
<div class="abs hero-stripe"></div>
<div class="abs caption cap1">LOREM IPSUM DOLOR SIT AMET</div>
<div class="abs caption cap2">CURABITUR HENDRERIT VEL</div>

<form class="abs search">
  <h2>Search Cruises</h2>
  <div class="sel" style="top:53px">Asia<i><svg width="9" height="6"><path d="M0 0 L9 0 L4.5 6Z" fill="#3a6ea5"/></svg></i></div>
  <div class="sel" style="top:92px">July 2013<i><svg width="9" height="6"><path d="M0 0 L9 0 L4.5 6Z" fill="#3a6ea5"/></svg></i></div>
  <div class="sel" style="top:132px">Any Length<i><svg width="9" height="6"><path d="M0 0 L9 0 L4.5 6Z" fill="#3a6ea5"/></svg></i></div>
  <div class="sel" style="top:172px">Any Cruise Line<i><svg width="9" height="6"><path d="M0 0 L9 0 L4.5 6Z" fill="#3a6ea5"/></svg></i></div>
  <span class="more">More than 10,000 routes for you</span>
  <span class="adv">Advance Search</span>
  <span class="go">Search</span>
</form>

<div class="abs tabbar"></div>
<ul class="abs tabs"><li class="on">Book with us</li><li>Deals</li><li>Packages</li><li>News</li><li>First time cruiser?</li></ul>

<section class="book">
  <div class="abs photo-frame"><div class="photo" role="img" aria-label="Happy guests jumping into a ship's pool"></div></div>
  <h1>Book With Us!</h1>
  <h3>It’s easy and fun</h3>
  <p>we’re the most advanced cruise booking provider in china.</p>
  <ul class="perks">
    <li><span class="tick"><svg width="8" height="6"><path d="M1 3 L3 5 L7 1" stroke="#fff" stroke-width="1.6" fill="none"/></svg></span>Great Prices</li>
    <li><span class="tick"><svg width="8" height="6"><path d="M1 3 L3 5 L7 1" stroke="#fff" stroke-width="1.6" fill="none"/></svg></span>Fast booking processing</li>
    <li><span class="tick"><svg width="8" height="6"><path d="M1 3 L3 5 L7 1" stroke="#fff" stroke-width="1.6" fill="none"/></svg></span>20 Cruise Lines</li>
    <li><span class="tick"><svg width="8" height="6"><path d="M1 3 L3 5 L7 1" stroke="#fff" stroke-width="1.6" fill="none"/></svg></span>Destination Around the World</li>
  </ul>
</section>

<aside class="abs news">
  <h4>Cruise Deals Newsletter</h4>
  <div class="nimg" role="img" aria-label="Friends playing in the surf at the beach"></div>
  <div class="sub">Subscribe to the best cruise deals now!</div>
  <div class="email"><svg width="16" height="10"><rect x=".5" y=".5" width="15" height="9" fill="none" stroke="#555"/><path d="M.5 .5 L8 6 L15.5 .5" fill="none" stroke="#555"/></svg>Your email here</div>
  <span class="subbtn">Subscribe</span>
</aside>

<h2 class="abs partners-h">Our Reliable Partners</h2>
<div class="abs badge" style="left:115px"><span style="background:#5d8aa8"></span></div>
<div class="abs badge" style="left:271px"><span style="background:var(--red)"></span></div>
<div class="abs badge" style="left:428px"><span style="background:#1d4a9c"></span></div>
<div class="abs badge" style="left:584px"><span style="background:#5d8aa8"></span></div>
<div class="abs badge" style="left:741px"><span style="background:var(--red)"></span></div>

<footer class="abs footer"></footer>
<div class="abs fcol" style="left:115px;top:975px"><h5>Useful Pages</h5>
  <ul><li>About us</li><li>Contact us</li><li>FAQ</li><li>Terms of service</li><li>Payment Info</li><li>Reward Points</li></ul></div>
<div class="abs fcol" style="left:304px;top:975px"><h5>Cruise Info</h5>
  <ul><li>Cruise news</li><li>Visa</li><li>Honeymoon Cruises</li><li>First time on a cruise</li></ul></div>
<div class="abs fcol" style="left:491px;top:975px"><h5>About bluewake.example</h5></div>
<div class="abs flogo"><span class="c"></span><b>Bluewake</b></div>
<div class="abs faddr" style="left:574px;top:1006px;width:82px">We’re the most Advance cruise booking provider in china.</div>
<div class="abs fcol" style="left:714px;top:975px;width:160px"><h5>Contact us</h5>
  <div class="faddr">Tidewater Studio Ltd. Harbour Centre Unit 12, 88 Quay Road, Portsmere 6425</div>
  <div class="fline" style="margin-top:10px"><svg width="10" height="11" viewBox="0 0 16 20"><path d="M4 1 L7 1 L8 6 L6 7 Q7 12 10 14 L12 12 L15 15 L14 18 Q6 18 3 10 Q1 4 4 1Z" fill="#888"/></svg>(021) 555 - 0142</div>
  <div class="fline" style="padding-left:16px">(021) 555 - 0187</div>
  <div class="fline"><svg width="10" height="8"><rect x=".5" y=".5" width="9" height="7" fill="#888"/><path d="M.5 .5 L5 4.5 L9.5 .5" stroke="#444" fill="none"/></svg>hello@bluewake.example</div>
</div>
<div class="abs fdivide"></div>
<div class="abs copy">Copyright © 2011 Bluewake. All rights reserved.<br>ICP No. 10000000</div>
<div class="abs foot-social"><span><i></i></span><span><i></i></span><span><i></i></span><span><i></i></span><span><i></i></span></div>

</body>
</html>
```